TrivoSuite – Veloura Flyer for Plexora (Harwick Travel Corporation)

Overview
Harwick Travel Corporation is launching a series of branded flyers to highlight the features and benefits of our TrivoSuite platform — our all-in-one corporate travel technology suite.
This first flyer will spotlight Veloura, our risk management and traveller safety solution, and will be published on Plexora as part of a digital awareness campaign.
⸻
Objective
Create a striking, professional, and modern flyer that communicates how Veloura enhances the TrivoSuite platform by ensuring traveller safety, communication, and real-time updates.
The design should feel premium, contemporary, and aligned with Harwick Travel’s luxury corporate identity.
⸻
Target Audience
• Corporate clients and travel decision-makers
• Travel managers, procurement teams, and executive assistants
• Existing Harwick Travel corporate partners on Plexora
⸻
Key Message
Veloura – Your travellers’ safety, visibility, and communication, all in one place.
Part of TrivoSuite, Harwick Travel’s integrated corporate travel platform.
⸻
Core Features to Highlight
• 24/7 real-time risk alerts
• Instant traveller identification and tracking by location or timeframe
• Two-way communication between traveller and company
• Integrated with travel itineraries for seamless care
• Supports duty-of-care compliance for corporate travel policies
⸻
Tone & Style
• Sophisticated, trusted, and innovative
• Clean lines, premium feel, and minimal clutter
• Should feel like a Harwick Travel-branded asset — not overly “techy”
• Imagery: travel safety, global maps, communication lines, or business travellers in motion
⸻
Design Direction
• Brand: Use Harwick Travel brand colours (gold, charcoal, white, navy)
• Typography: Professional, modern sans-serif fonts
• Logo: Include Harwick Travel and TrivoSuite logos (can supply if needed)
• CTA: “Discover Veloura on TrivoSuite” or “Set the Gold Standard of Corporate Travel”
• Layout: Ideal for Plexora post format (square or 4:5 vertical)
⸻
Deliverables
• Editable design file (AI / PSD / InDesign)
• Final exports for social media:
• 1080x1080 px (Plexora square)
• 1080x1350 px (Plexora portrait)
• Include space for light text overlay (for post captioning later)
⸻
Inspiration
• Style similar to luxury tech or premium corporate innovation brands
• Feel: clean, high-contrast, aspirational, minimal

```html
<!DOCTYPE html>
<html lang="en">
<head>
<meta charset="utf-8">
<title>TrivoSuite – Veloura Flyer</title>
<link rel="stylesheet" href="https://fonts.googleapis.com/css2?family=Poppins:wght@400;500;600;700;800&family=Inter:wght@500;600&display=swap">
<style>
  :root {
    --canvas: #e9e9e9;
    --navy-deep: #0d1733;
    --navy: #1c2650;
    --mauve: #5a4a6e;
    --dusk: #7a5f78;
    --gold: #dca35a;
    --white: #ffffff;
    --band-top: #141619;
    --band-bottom: #6a4636;
  }
  * { margin: 0; padding: 0; box-sizing: border-box; }
  html, body {
    width: 1200px;
    height: 2484px;
    overflow: hidden;
    background: var(--canvas);
  }
  .flyer {
    position: absolute;
    left: 107px;
    top: 750px;
    width: 985px;
    height: 985px;
    overflow: hidden;
    color: var(--white);
    font-family: "Poppins", sans-serif;
    background: var(--navy-deep);
  }
  .flyer__backdrop {
    position: absolute;
    inset: 0;
    background:
      radial-gradient(ellipse 60% 35% at 75% 55%, rgba(150,110,140,0.55), transparent 70%),
      radial-gradient(ellipse 40% 40% at 15% 70%, rgba(120,100,120,0.55), transparent 70%),
      linear-gradient(180deg, #0d1733 0%, #1e2754 30%, #45406a 55%, #5a4a6e 68%, #2c2f5a 85%, #1a2450 100%);
  }
  .flyer__band {
    position: absolute;
    left: 680px;
    top: 0;
    width: 220px;
    height: 655px;
    background: linear-gradient(180deg, var(--band-top) 0%, #1d1b1f 35%, #4b3430 70%, var(--band-bottom) 100%);
    opacity: 0.92;
  }
  .brand {
    position: absolute;
    left: 67px;
    top: 50px;
  }
  .brand__name {
    font-family: "Poppins", sans-serif;
    font-weight: 800;
    font-size: 44px;
    line-height: 1;
    color: var(--gold);
    letter-spacing: 0.5px;
  }
  .brand__corp {
    margin-top: 8px;
    font-family: "Inter", sans-serif;
    font-weight: 600;
    font-size: 17px;
    letter-spacing: 0.3px;
    text-transform: uppercase;
  }
  .headline {
    position: absolute;
    left: 64px;
    top: 200px;
    font-weight: 700;
    font-size: 100px;
    line-height: 85px;
    letter-spacing: -1px;
    text-transform: uppercase;
  }
  .headline__accent { color: var(--gold); display: block; }
  .headline span { display: block; }
  .intro {
    position: absolute;
    left: 67px;
    top: 484px;
    width: 340px;
    font-size: 17.5px;
    line-height: 22.3px;
    font-weight: 400;
  }
  .intro strong { font-weight: 600; }
  .features {
    position: absolute;
    left: 67px;
    top: 678px;
    list-style: none;
    width: 360px;
  }
  .features__item {
    position: relative;
    padding-left: 22px;
    font-size: 17px;
    line-height: 20.5px;
    font-weight: 500;
    margin-bottom: 20px;
  }
  .features__icon {
    position: absolute;
    left: 0;
    top: 3px;
    width: 14px;
    height: 14px;
  }
  .devices {
    position: absolute;
    left: 615px;
    top: 665px;
    width: 315px;
    height: 215px;
    border-radius: 6px;
    background: linear-gradient(160deg, #e8eaf0 0%, #c9ccd6 55%, #9ea3b4 100%);
    opacity: 0.9;
  }
  .cta {
    position: absolute;
    right: 55px;
    top: 888px;
    text-align: right;
    font-weight: 700;
    font-size: 27px;
    line-height: 28px;
    color: var(--gold);
    text-transform: uppercase;
  }
</style>
</head>
<body>
  <section class="flyer">
    <div class="flyer__backdrop" role="img" aria-label="Photo of a passenger jet flying above dusk clouds beside a rocky mountain cliff"></div>
    <div class="flyer__band"></div>

    <header class="brand">
      <div class="brand__name">TrivoSuite</div>
      <div class="brand__corp">Harwick Travel Corporation</div>
    </header>

    <h1 class="headline">
      <span>Harwick</span>
      <span class="headline__accent">Travel’s</span>
      <span>Luxury</span>
    </h1>

    <p class="intro"><strong>Veloura</strong> offers 24/7 monitoring making sure you are updated of any issues that occur. With risk alerts, traveller identification and two-way communication the duty of care tool reduces problems with ease.</p>

    <ul class="features">
      <li class="features__item"><svg class="features__icon" viewBox="0 0 14 14"><circle cx="7" cy="7" r="6" fill="none" stroke="#dca35a" stroke-width="1.6"/><path d="M4 7.2l2 2 4-4.2" fill="none" stroke="#dca35a" stroke-width="1.6" stroke-linecap="round" stroke-linejoin="round"/></svg>24/7 Real-Time Risk Alerts</li>
      <li class="features__item"><svg class="features__icon" viewBox="0 0 14 14"><circle cx="7" cy="7" r="6" fill="none" stroke="#dca35a" stroke-width="1.6"/><path d="M4 7.2l2 2 4-4.2" fill="none" stroke="#dca35a" stroke-width="1.6" stroke-linecap="round" stroke-linejoin="round"/></svg>Instant Traveller Identification and Tracking By Location or Timeframe</li>
      <li class="features__item"><svg class="features__icon" viewBox="0 0 14 14"><circle cx="7" cy="7" r="6" fill="none" stroke="#dca35a" stroke-width="1.6"/><path d="M4 7.2l2 2 4-4.2" fill="none" stroke="#dca35a" stroke-width="1.6" stroke-linecap="round" stroke-linejoin="round"/></svg>Two-Way Communication Between Traveller and Company</li>
      <li class="features__item"><svg class="features__icon" viewBox="0 0 14 14"><circle cx="7" cy="7" r="6" fill="none" stroke="#dca35a" stroke-width="1.6"/><path d="M4 7.2l2 2 4-4.2" fill="none" stroke="#dca35a" stroke-width="1.6" stroke-linecap="round" stroke-linejoin="round"/></svg>Integrated with Travel Itineraries for Seamless Care</li>
      <li class="features__item"><svg class="features__icon" viewBox="0 0 14 14"><circle cx="7" cy="7" r="6" fill="none" stroke="#dca35a" stroke-width="1.6"/><path d="M4 7.2l2 2 4-4.2" fill="none" stroke="#dca35a" stroke-width="1.6" stroke-linecap="round" stroke-linejoin="round"/></svg>Supports Duty-of-Care Compliance for Corporate Travel Policies</li>
    </ul>

    <div class="devices" role="img" aria-label="Desktop monitor, laptop and smartphone showing the Veloura traveller dashboard"></div>

    <p class="cta">Discover Veloura<br>on TrivoSuite</p>
  </section>
</body>
</html>
```